Business Cards

Now that we have a fantastic logo, we need business cards designed for our organization.
We'd like a design that uses our logo and is very creative and eye catching. It should have the following copy, in addition to our logo. It can be standard business card size, or smaller.
Cultivate. Connect. Create.
1128 Pelham Avenue
Ashcombe, Farrowdale
Harwick County
California
Commonwealth of Veloria
url: www.larkspurrowguild.org
twitter: #larkspurcraft
facebook, linkedin, google+, and tumblr: larkspur row guild
email: info@larkspurrowguild

```html
<!DOCTYPE html>
<html lang="en">
<head>
<meta charset="utf-8">
<title>Larkspur Row Guild — Business Card</title>
<link rel="stylesheet" href="https://fonts.googleapis.com/css2?family=Lato:ital,wght@0,300;1,300&display=swap">
<style>
  :root {
    --paper: #ffffff;
    --tangerine: #ec7b3a;
    --harbour-blue: #1b6799;
  }
  html, body {
    margin: 0;
    padding: 0;
    width: 686px;
    height: 1200px;
    overflow: hidden;
    background: var(--paper);
  }
  .card-sheet {
    position: relative;
    width: 686px;
    height: 1200px;
    font-family: "Lato", "Gill Sans", sans-serif;
    font-weight: 300;
  }
  .tile {
    position: absolute;
    left: 88px;
    width: 510px;
    height: 511px;
    border-radius: 132px;
    box-sizing: border-box;
  }
  .tile--contact {
    top: 64px;
    background: var(--tangerine);
  }
  .tile--address {
    top: 624px;
    background: var(--harbour-blue);
  }
  .contact-run {
    position: absolute;
    left: 38px;
    top: 102px;
    width: 434px;
    margin: 0;
    color: var(--harbour-blue);
    font-style: italic;
    font-size: 28px;
    letter-spacing: -0.4px;
    line-height: 62px;
    word-break: break-all;
    text-align: left;
  }
  .address {
    position: absolute;
    left: 0;
    right: 0;
    top: 116px;
    margin: 0;
    text-align: center;
    color: var(--tangerine);
    font-style: normal;
  }
  .address span { display: block; white-space: nowrap; }
  .address__street  { font-size: 45px; line-height: 64px; }
  .address__city    { font-size: 46px; line-height: 64px; }
  .address__county  { font-size: 42px; line-height: 60px; }
  .address__country { font-size: 32px; line-height: 52px; }
</style>
</head>
<body>
  <main class="card-sheet">
    <section class="tile tile--contact">
      <p class="contact-run">url: www.larkspurrowguild.org : : twitter: #larkspurcraft : : facebook, linkedin, google+, and tumblr: larkspur row guild : : email: info@larkspurrowguild : :</p>
    </section>
    <section class="tile tile--address">
      <address class="address">
        <span class="address__street">1128 Pelham Avenue</span>
        <span class="address__city">Ashcombe, Farrowdale</span>
        <span class="address__county">Harwick County</span>
        <span class="address__country">Commonwealth of Veloria</span>
      </address>
    </section>
  </main>
</body>
</html>
```